UK garage/funky house night flier

I need a flier design to upload to my sociallink event page and also some printed fliers to promote the event.

Event is in an urban area underneath railway arches so would like a flier to reflect this with an urban background.

new photos uploaded to be used as possible backgrounds

Target Market(s)

aged 18-30

Industry/Entity Type

House

Requirements
Must have
• The following text on front of flier:

TRUE PULSE ENTERTAINMENTS PRESENTS A NIGHT CALLED…

‘MIDNIGHT CELLAR RHYTHMZ’

Saturday 7th September 2013

@ Dock47, Harlow Lane, Digbeth, Birmingham B9 3QW

9pm till late

DJ’s playing a selection of Funky house/deep house/future garage and old school 2-step garage

(On back of flier......)

Come and enjoy yourself in a friendly, safe environment with like-minded people who are out to have a good time and rave till the early hours. This venue is part outdoor terrace and part indoor with music being played on the Wavecraft Soundsystem – so you know it is a night not to be missed!!

This event is guestlist only. Those not on the guest list will not be allowed entry. To get yourself on the guest list go to the sociallink page www.sociallink.example/truepulseentertainments and join the event ‘Midnight Cellar Rhythmz’

Dresscode: smart. No trainers/tracksuits
Admission fee on the door is £5
Last entry: midnight
Nice to have
• must be portrait, A5 or A6 size

Urban background, maybe at night, a street with old brickwork, maybe some speakers in the foreground.

dock47 logo bottom right

Back of flier to have the map of Dock47

```html
<!DOCTYPE html>
<html lang="en">
<head>
<meta charset="utf-8">
<title>Midnight Cellar Rhythmz – Flier Front and Back</title>
<link rel="stylesheet" href="https://fonts.googleapis.com/css2?family=Audiowide&family=Russo+One&family=Montserrat:wght@600;700&family=Raleway:wght@300;400&display=swap">
<style>
  :root {
    --page: #ebe8e1;
    --night: #0d1022;
    --dusk: #2a1a2e;
    --brick: #7a2f14;
    --ember: #b4501f;
    --glow: #c9663a;
    --sun: rgba(196, 52, 38, 0.72);
    --ink: #ffffff;
    --ink-soft: #e7e4ee;
    --chrome-edge: #7c7f8a;
    --rule: rgba(150, 60, 40, 0.8);
    --map: #f2f2f2;
  }
  * { margin: 0; padding: 0; box-sizing: border-box; }
  html, body { width: 1200px; height: 1000px; overflow: hidden; }
  body { background: var(--page); position: relative; font-family: "Montserrat", sans-serif; color: var(--ink); }

  .flier { position: absolute; overflow: hidden; box-shadow: 2px 3px 8px rgba(0,0,0,0.35); }
  .flier-front { left: 28px; top: 30px; width: 492px; height: 732px; }
  .flier-back { left: 634px; top: 232px; width: 467px; height: 733px; }

  .backdrop {
    position: absolute; inset: 0;
    background:
      radial-gradient(ellipse 60% 35% at 70% 55%, rgba(70, 90, 220, 0.35), transparent 70%),
      linear-gradient(180deg, var(--night) 0%, var(--dusk) 28%, var(--brick) 55%, var(--ember) 78%, var(--glow) 100%);
  }

  /* Front */
  .presenter {
    position: absolute; left: 0; right: 0; top: 16px;
    text-align: center; font-weight: 600; font-size: 15px;
    letter-spacing: 1.4px; line-height: 24px; padding-left: 30px;
  }
  .sun { position: absolute; left: 140px; top: 100px; width: 140px; height: 140px; border-radius: 50%; background: var(--sun); }
  .title {
    position: absolute; left: 110px; width: 370px; top: 168px;
    text-align: center; font-family: "Audiowide", sans-serif;
    font-size: 46px; line-height: 56px; letter-spacing: 1px;
    color: var(--ink); text-shadow: 1px 2px 0 var(--chrome-edge), 2px 4px 3px rgba(0,0,0,0.6);
  }
  .title-rule { position: absolute; left: 176px; top: 322px; width: 196px; height: 2px; background: var(--ink); }
  .hours { position: absolute; left: 110px; width: 370px; top: 332px; text-align: center; font-family: "Raleway", sans-serif; font-size: 25px; font-weight: 400; }
  .date {
    position: absolute; left: 0; right: 0; top: 495px; text-align: center;
    font-family: "Russo One", sans-serif; font-size: 40px; letter-spacing: 3px;
    text-shadow: 2px 2px 0 rgba(0,0,0,0.45);
  }
  .lineup { position: absolute; left: 0; right: 0; top: 563px; text-align: center; font-weight: 700; font-size: 14.5px; line-height: 23.5px; letter-spacing: 0.4px; }
  .venue-mark { position: absolute; left: 72px; top: 684px; display: flex; align-items: center; gap: 6px; font-weight: 700; font-size: 16px; }
  .venue-mark .dot { width: 10px; height: 10px; background: var(--ink); }
  .venue-address { position: absolute; left: 177px; top: 680px; font-family: "Raleway", sans-serif; font-size: 16px; line-height: 23px; }

  /* Back */
  .pitch {
    position: absolute; left: 69px; top: 45px; width: 388px;
    font-family: "Raleway", sans-serif; font-weight: 300; font-size: 15.5px; line-height: 24.6px; color: var(--ink-soft);
  }
  .entry-panel {
    position: absolute; left: 63px; top: 206px; width: 396px; height: 264px;
    border: 1px solid var(--rule); background: rgba(10, 10, 20, 0.25);
    padding: 6px 8px; font-family: "Raleway", sans-serif; font-size: 14px; line-height: 23.5px; color: var(--ink-soft);
  }
  .entry-panel p + p { margin-top: 23.5px; }
  .entry-panel .details { margin-top: 6px; }
  .venue-map { position: absolute; left: 61px; top: 470px; width: 393px; height: 263px; background: linear-gradient(160deg, var(--map), #dcdcdc); }
</style>
</head>
<body>
  <section class="flier flier-front">
    <div class="backdrop" role="img" aria-label="Night photograph of brick railway arches on an urban street with blue light trails"></div>
    <p class="presenter">TRUE PULSE ENTERTAINMENTS<br>PRESENTS A NIGHT CALLED…</p>
    <div class="sun"></div>
    <h1 class="title">MIDNIGHT<br>CELLAR<br>RHYTHMZ</h1>
    <div class="title-rule"></div>
    <p class="hours">9pm till late</p>
    <p class="date">SAT. 7TH. SEP.</p>
    <p class="lineup">DJ’S PLAYING A SELECTION OF<br>FUNKY HOUSE/DEEP HOUSE/FUTURE GARAGE<br>AND OLD SCHOOL 2-STEP GARAGE</p>
    <div class="venue-mark"><span class="dot"></span><span>DOCK47</span></div>
    <p class="venue-address">@ Dock47, Harlow Lane,<br>Digbeth, Birmingham B9 3QW</p>
  </section>

  <section class="flier flier-back">
    <div class="backdrop" role="img" aria-label="Night photograph of brick railway arches with blue light trails"></div>
    <p class="pitch">Come and enjoy yourself in a friendly, safe environment with like-minded people who are out to have a good time and rave till the early hours. This venue is part outdoor terrace and part indoor with music being played on the Wavecraft Soundsystem – so you know it is a night not to be missed!!</p>
    <div class="entry-panel">
      <p>THIS EVENT IS GUESTLIST ONLY.<br>Those not on the guest list will not be allowed entry.</p>
      <p>TO GET YOURSELF ON THE GUEST LIST GO TO<br>THE SOCIALLINK PAGE<br>www.sociallink.example/truepulseentertainments<br>and join the event ‘Midnight Cellar Rhythmz’</p>
      <p class="details">DRESSCODE: SMART. NO TRAINERS/TRACKSUITS<br>ADMISSION FEE ON THE DOOR IS £5<br>LAST ENTRY: MIDNIGHT</p>
    </div>
    <div class="venue-map" role="img" aria-label="Street map of Digbeth showing the route to Dock47 with venue details"></div>
  </section>
</body>
</html>
```